Business Card Design Project

I want a design for my business cards based on an excisting logo design.

Target Market(s)

Marketeers, PR-peeps, CEO's, decisionmakers, entrepreneurs

Industry/Entity Type

Business

Requirements
Nice to have
• Some visual interest on the back too
Should not have
• Sarif on the font

```html
<!DOCTYPE html>
<html lang="en">
<head>
<meta charset="utf-8">
<title>LeafTone business cards</title>
<link rel="stylesheet" href="https://fonts.googleapis.com/css2?family=Open+Sans:wght@400;700;800&family=Gochi+Hand&display=swap">
<style>
  :root {
    --leaf-green: #12a04a;
    --leaf-green-dark: #0a8a3c;
    --leaf-lime: #8cc63f;
    --leaf-glow: #5cc05a;
    --paper: #ffffff;
    --ink: #333333;
    --muted: #666666;
    --stage: #e9ebe8;
  }
  * { margin: 0; padding: 0; box-sizing: border-box; }
  html, body { width: 1200px; height: 900px; overflow: hidden; }
  body {
    background: var(--stage);
    font-family: "Open Sans", Arial, sans-serif;
    position: relative;
  }
  .card {
    position: absolute;
    width: 560px;
    height: 320px;
    border-radius: 22px;
    overflow: hidden;
    box-shadow: 0 10px 28px rgba(0,0,0,0.18);
  }

  /* Front of card */
  .card-front {
    left: 60px;
    top: 90px;
    background: radial-gradient(circle at 50% 32%, var(--leaf-glow) 0%, var(--leaf-green) 45%, var(--leaf-green-dark) 100%);
  }
  .front-mark {
    position: absolute;
    left: 50%;
    top: 34px;
    width: 96px;
    height: 96px;
    margin-left: -48px;
    border-radius: 50%;
    background: var(--leaf-lime);
  }
  .front-brand {
    position: absolute;
    left: 0; right: 0;
    top: 138px;
    text-align: center;
    font-size: 54px;
    font-weight: 400;
    letter-spacing: 2px;
    color: var(--paper);
  }
  .front-band {
    position: absolute;
    left: 0; right: 0;
    top: 218px;
    height: 34px;
    background: var(--paper);
    text-align: center;
    line-height: 34px;
    font-size: 15px;
    color: var(--leaf-green);
  }

  /* Back of card */
  .card-back {
    left: 580px;
    top: 470px;
    background: var(--paper);
  }
  .back-edge-top {
    position: absolute;
    right: 0; top: 0;
    width: 150px; height: 8px;
    background: var(--leaf-green);
    border-bottom-left-radius: 8px;
  }
  .back-edge-bottom {
    position: absolute;
    right: 0; bottom: 0;
    width: 260px; height: 10px;
    background: var(--leaf-green);
    border-top-left-radius: 10px;
  }
  .back-logo {
    position: absolute;
    left: 28px; top: 24px;
    display: flex;
    align-items: center;
    gap: 12px;
  }
  .back-logo-mark {
    width: 56px; height: 56px;
    border-radius: 50%;
    background: var(--leaf-lime);
  }
  .back-logo-name {
    font-size: 34px;
    font-weight: 400;
    letter-spacing: 1px;
    color: var(--muted);
  }
  .person {
    position: absolute;
    left: 30px; top: 98px;
  }
  .person-name {
    font-size: 24px;
    font-weight: 800;
    color: var(--leaf-green);
    line-height: 1.1;
  }
  .person-role {
    font-size: 10px;
    font-weight: 700;
    color: var(--ink);
    margin-left: 2px;
  }
  .address {
    position: absolute;
    left: 30px; top: 160px;
    font-family: "Gochi Hand", cursive;
    font-size: 17px;
    color: var(--ink);
  }
  .contacts {
    position: absolute;
    left: 30px; top: 188px;
    list-style: none;
    display: grid;
    grid-template-columns: 190px 260px;
    grid-template-rows: repeat(3, 28px);
    grid-auto-flow: column;
  }
  .contacts li {
    display: flex;
    align-items: center;
    gap: 14px;
    font-family: "Gochi Hand", cursive;
    font-size: 17px;
    color: var(--ink);
  }
  .contacts .skip { visibility: hidden; }
  .icon { width: 18px; height: 18px; flex: none; }
  .social-square {
    width: 18px; height: 18px; flex: none;
    border-radius: 4px;
    background: var(--leaf-green);
  }
</style>
</head>
<body>

  <section class="card card-front" aria-label="Card front">
    <div class="front-mark"></div>
    <div class="front-brand">LeafTone</div>
    <div class="front-band">leaftone.nl</div>
  </section>

  <section class="card card-back" aria-label="Card back">
    <div class="back-edge-top"></div>
    <div class="back-edge-bottom"></div>

    <div class="back-logo">
      <div class="back-logo-mark"></div>
      <div class="back-logo-name">LeafTone</div>
    </div>

    <div class="person">
      <div class="person-name">Maren Holt</div>
      <div class="person-role">General Manager</div>
    </div>

    <div class="address">Lindelaan 12 4811 AB Breda</div>

    <ul class="contacts">
      <li>
        <svg class="icon" viewBox="0 0 18 18" aria-hidden="true">
          <rect x="1" y="1" width="16" height="16" rx="3" fill="var(--leaf-green)"/>
          <rect x="6" y="3.5" width="6" height="11" rx="1.2" fill="none" stroke="#fff" stroke-width="1.4"/>
          <circle cx="9" cy="12.4" r="0.8" fill="#fff"/>
        </svg>
        +31(0)6 20481357
      </li>
      <li><span class="social-square"></span>leaftone</li>
      <li><span class="social-square"></span>/_leaftone</li>
      <li class="skip"></li>
      <li>
        <svg class="icon" viewBox="0 0 18 18" aria-hidden="true">
          <circle cx="9" cy="9" r="8" fill="var(--leaf-green)"/>
          <ellipse cx="9" cy="9" rx="3.4" ry="7.2" fill="none" stroke="#fff" stroke-width="1.2"/>
          <line x1="1.8" y1="9" x2="16.2" y2="9" stroke="#fff" stroke-width="1.2"/>
        </svg>
        leaftone.nl
      </li>
      <li>
        <svg class="icon" viewBox="0 0 18 18" aria-hidden="true">
          <rect x="1" y="3.5" width="16" height="11" rx="1.5" fill="var(--leaf-green)"/>
          <polyline points="1.8,4.5 9,10 16.2,4.5" fill="none" stroke="#fff" stroke-width="1.3"/>
        </svg>
        maren.holt@leaftone.nl
      </li>
    </ul>
  </section>

</body>
</html>
```